Flyer for Merchant Capital Cash Advance business

Need Flyer Design to be advertised on Social Media Platforms and also Print it to Publish it in Magazines.
Flyer Will be printed in different sizes for different publications.
Size 1) 6.25 inches * 11 inches.
Size 2) 8 inch * 11 inch
Size 3) 8 inch * 5.5 I inch
Size 4) 5 inch * 7 inch.
Google “Merchant Capital Cash advance flyer pics” to get an idea.

Flyer Design for Merchant Cash advance business.

Merchant Cash Advance is alternate to bank loans and does not require Personal Guarantee or Collateral.
Updates

Need extra days to review

Target Market(s)

Business owners seeking loan.

Industry/Entity Type

Business Service

Font styles to use
Serif
Sans Serif
Decorative
Script

Colors

Designer to choose colors to be used in the design.

Requirements
Must have
• Content from the Files Uploaded.
• Sharp Colors.
Nice to have
• Would like to see flyer in shape of a Bank Check or a $100 Bill.
• Would like to show a Comparison between Bank Loan and MCA.
• Open to any other ideas.

```html
<!DOCTYPE html>
<html lang="en">
<head>
<meta charset="utf-8">
<title>Merchant Cash Advance Flyer – Size Set</title>
<link rel="stylesheet" href="https://fonts.googleapis.com/css2?family=Titillium+Web:ital,wght@0,600;1,600;1,700&family=Roboto:ital,wght@0,400;0,500;0,700;1,400;1,500&family=Oswald:wght@500&family=EB+Garamond:wght@400&display=swap">
<style>
  :root{
    --lime:#b6d335;
    --lime-block:#c6dd79;
    --green-soft:#d3e8c4;
    --green-pale:#e1efd0;
    --blue:#37a5dd;
    --blue-deep:#1a78bd;
    --sky:#d2ebf6;
    --sky-pale:#e7f4fa;
    --orange:#e8683a;
    --charcoal:#3d3d40;
    --grey-text:#cfcfcf;
    --white:#ffffff;
  }
  *{box-sizing:border-box;margin:0;padding:0}
  html,body{width:900px;height:1200px;overflow:hidden}
  body{
    position:relative;
    font-family:"Roboto",Arial,sans-serif;
    background:linear-gradient(180deg,var(--white) 0 45px,#e9e9ea 45px,#f7f7f7 55%,#ebebec 100%);
  }
  .flyer{position:absolute;overflow:hidden;box-shadow:0 4px 10px rgba(0,0,0,.35);background:var(--sky-pale)}
  .flyer > *{position:absolute}
  .photo{
    left:0;top:0;width:100%;
    background:
      radial-gradient(ellipse at 78% 55%,rgba(70,100,50,.9),rgba(70,100,50,0) 60%),
      linear-gradient(135deg,#6c6f97 0%,#7c8080 45%,#61784c 75%,#4d6a39 100%);
  }
  .headline{
    font-family:"Titillium Web",Arial,sans-serif;font-style:italic;font-weight:700;
    color:var(--lime);white-space:nowrap;letter-spacing:-.5px;
  }
  .headline .borrow{color:var(--blue)}
  .tagline{
    background:rgba(55,55,60,.6);color:var(--blue);font-style:italic;font-weight:500;
    line-height:1.35;white-space:nowrap;
  }
  .block{display:block}
  .mca{color:var(--blue-deep);font-weight:500;line-height:1}
  .benefit{color:var(--blue-deep);font-weight:500;white-space:nowrap;text-transform:uppercase;display:flex;align-items:center}
  .benefit svg{flex:none}
  .bank-head{background:var(--lime-block);color:var(--blue-deep);text-align:center;font-weight:500;line-height:1.1;display:flex;flex-direction:column;justify-content:center}
  .cross{display:block}
  .apply{color:var(--orange);white-space:nowrap;text-transform:uppercase}
  .inquire{color:var(--orange);font-style:italic;white-space:nowrap}
  .inquire b{font-weight:500}
  .bar{left:0;width:100%;background:var(--charcoal);color:var(--white)}
  .bar-title{position:absolute;font-family:"Oswald",sans-serif;font-weight:500;letter-spacing:-.3px;white-space:nowrap;transform:scaleX(.86);transform-origin:left center}
  .call{position:absolute;white-space:nowrap}
  .call em{display:block;font-family:"Roboto",sans-serif;font-style:italic;font-weight:500}
  .call .phone{display:block;font-family:"EB Garamond",Georgia,serif;font-variant-numeric:oldstyle-nums;letter-spacing:.5px}
  .stacked-title{
    color:var(--grey-text);font-family:"Oswald",sans-serif;font-weight:500;
    text-align:center;white-space:nowrap;transform:scaleX(.82);transform-origin:center center;
  }
  .size-label{position:absolute;transform:translateX(-50%);font-weight:700;color:var(--blue);font-size:45px;line-height:1;white-space:nowrap}
</style>
</head>
<body>

<svg width="0" height="0" style="position:absolute" aria-hidden="true">
  <symbol id="tick" viewBox="0 0 24 20"><path d="M1 10 L8 18 L23 2" fill="none" stroke="#a8cc3a" stroke-width="3"/></symbol>
  <symbol id="cross" viewBox="0 0 20 20"><path d="M3 3 L17 17 M17 3 L3 17" stroke="#e8683a" stroke-width="2.2" fill="none"/></symbol>
</svg>

<!-- 8 x 11 -->
<section class="flyer" style="left:41px;top:32px;width:432px;height:595px">
  <div class="photo" role="img" aria-label="Close-up photograph of a fan of hundred dollar banknotes" style="height:289px"></div>
  <div class="headline" style="left:27px;top:14px;font-size:46px;line-height:56px">
    <span class="block">Say “Hello”</span><span class="block">To A</span><span class="block">Better Way</span><span class="block">To <span class="borrow">BORROW</span></span>
  </div>
  <div class="tagline" style="left:197px;top:245px;width:235px;height:32px;padding:2px 6px;font-size:12px">A convenient alternative to Bank Loan<br>Get Business Capital Cash Advance</div>

  <div style="left:0;top:319px;width:372px;height:163px;background:var(--sky)"></div>
  <div style="left:0;top:373px;width:56px;height:109px;background:var(--green-soft)"></div>
  <div style="left:0;top:482px;width:56px;height:59px;background:var(--lime-block)"></div>
  <div style="left:372px;top:289px;width:60px;height:252px;background:var(--white)"></div>
  <div style="left:372px;top:349px;width:60px;height:101px;background:var(--green-pale)"></div>
  <div class="bank-head" style="left:372px;top:289px;width:60px;height:60px;font-size:15px"><span>BANK</span><span>LOAN</span></div>

  <div class="mca" style="left:86px;top:326px;font-size:34px">MCA</div>
  <div class="benefit" style="left:152px;top:352px;font-size:8.5px"><svg width="18" height="17"><use href="#tick"/></svg>No personal guarantee</div>
  <div class="benefit" style="left:152px;top:376px;font-size:8.5px"><svg width="18" height="17"><use href="#tick"/></svg>No minimum credit score</div>
  <div class="benefit" style="left:152px;top:400px;font-size:8.5px"><svg width="18" height="17"><use href="#tick"/></svg>No collateral or guarantors needed</div>
  <div class="benefit" style="left:152px;top:425px;font-size:8.5px"><svg width="18" height="17"><use href="#tick"/></svg>Bankruptcy – OK</div>
  <svg class="cross" style="left:392px;top:353px" width="20" height="20"><use href="#cross"/></svg>
  <svg class="cross" style="left:392px;top:376px" width="20" height="20"><use href="#cross"/></svg>
  <svg class="cross" style="left:392px;top:400px" width="20" height="20"><use href="#cross"/></svg>
  <svg class="cross" style="left:392px;top:423px" width="20" height="20"><use href="#cross"/></svg>

  <div class="apply" style="left:77px;top:455px;font-size:16.5px">Simple one page application</div>
  <div class="inquire" style="left:62px;top:514px;font-size:8px;line-height:1.2">Inquire at<br><b style="font-size:12px">funding@example.com</b></div>

  <div class="bar" style="top:541px;height:54px">
    <span class="bar-title" style="left:14px;top:9px;font-size:27px">MERCHANT CASH ADVANCE</span>
    <span class="call" style="left:275px;top:4px"><em style="font-size:13.5px">Call Now</em><span class="phone" style="font-size:20px;line-height:1.1">555 013 2740</span></span>
  </div>
</section>
<div class="size-label" style="left:251px;top:646px">8X11</div>

<!-- 6.25 x 11 -->
<section class="flyer" style="left:515px;top:33px;width:338px;height:594px">
  <div class="photo" role="img" aria-label="Close-up photograph of a fan of hundred dollar banknotes" style="height:225px"></div>
  <div class="headline" style="left:22px;top:10px;font-size:37px;line-height:43.5px">
    <span class="block">Say “Hello”</span><span class="block">To A</span><span class="block">Better Way</span><span class="block">To <span class="borrow">BORROW</span></span>
  </div>
  <div class="tagline" style="left:155px;top:184px;width:183px;height:26px;padding:1px 5px;font-size:9.5px">A convenient alternative to Bank Loan<br>Get Business Capital Cash Advance</div>

  <div style="left:0;top:225px;width:290px;height:23px;background:var(--white)"></div>
  <div style="left:0;top:510px;width:338px;height:30px;background:var(--white)"></div>
  <div style="left:0;top:290px;width:43px;height:86px;background:var(--green-soft)"></div>
  <div style="left:0;top:376px;width:43px;height:46px;background:var(--lime-block)"></div>
  <div style="left:247px;top:464px;width:91px;height:76px;background:var(--green-pale)"></div>
  <div style="left:290px;top:271px;width:48px;height:137px;background:var(--green-pale)"></div>
  <div style="left:290px;top:408px;width:48px;height:79px;background:#c8e08c"></div>
  <div class="bank-head" style="left:290px;top:225px;width:48px;height:46px;font-size:12px"><span>BANK</span><span>LOAN</span></div>

  <div class="mca" style="left:60px;top:256px;font-size:30px">MCA</div>
  <div class="benefit" style="left:118px;top:285px;font-size:7px"><svg width="16" height="15"><use href="#tick"/></svg>No personal guarantee</div>
  <div class="benefit" style="left:118px;top:314px;font-size:7px"><svg width="16" height="15"><use href="#tick"/></svg>No minimum credit score</div>
  <div class="benefit" style="left:118px;top:343px;font-size:7px"><svg width="16" height="15"><use href="#tick"/></svg>No collateral or guarantors needed</div>
  <div class="benefit" style="left:118px;top:372px;font-size:7px"><svg width="16" height="15"><use href="#tick"/></svg>Bankruptcy – OK</div>
  <svg class="cross" style="left:306px;top:285px" width="16" height="16"><use href="#cross"/></svg>
  <svg class="cross" style="left:306px;top:315px" width="16" height="16"><use href="#cross"/></svg>
  <svg class="cross" style="left:306px;top:343px" width="16" height="16"><use href="#cross"/></svg>
  <svg class="cross" style="left:306px;top:372px" width="16" height="16"><use href="#cross"/></svg>

  <div class="apply" style="left:60px;top:415px;font-size:13px">Simple one page application</div>
  <div class="inquire" style="left:10px;top:520px;font-size:6.5px">Inquire at &nbsp;<b style="font-size:10px">funding@example.com</b></div>

  <div class="bar" style="top:540px;height:54px">
    <span class="bar-title" style="left:10px;top:10px;font-size:22px">MERCHANT CASH ADVANCE</span>
    <span class="call" style="left:215px;top:7px"><em style="font-size:11px">Call Now</em><span class="phone" style="font-size:17px;line-height:1.1;padding-left:22px">555 013 2740</span></span>
  </div>
</section>
<div class="size-label" style="left:696px;top:646px">6.25X11</div>

<!-- 8 x 5.5 -->
<section class="flyer" style="left:37px;top:726px;width:432px;height:297px">
  <div class="photo" role="img" aria-label="Close-up photograph of a fan of hundred dollar banknotes" style="height:297px"></div>
  <div class="headline" style="left:20px;top:9px;font-size:28px;line-height:31.5px">
    <span class="block">Say “Hello”</span><span class="block">To A</span><span class="block">Better Way</span><span class="block">To <span class="borrow">BORROW</span></span>
  </div>
  <div class="tagline" style="left:0;top:136px;width:240px;height:33px;padding:1px 0 0 20px;font-size:12px;line-height:1.4">A convenient alternative to Bank Loan<br>Get Business Capital Cash Advance</div>
  <div style="left:0;top:169px;width:432px;height:128px;background:rgba(58,58,62,.93)"></div>

  <div style="right:16px;top:17px;text-align:right;color:#e6e6ea;font-style:italic;line-height:1.3">
    <span class="block" style="font-size:10px">Call Now</span>
    <span class="block" style="font-size:15px">555 013 2740</span>
    <span class="block" style="font-size:10.5px">Inquire at</span>
    <span class="block" style="font-size:10px">funding@example.com</span>
  </div>

  <div class="stacked-title" style="left:5px;top:196px;width:200px;font-size:26px;line-height:37px">MERCHANT<br>CASH ADVANCE</div>

  <div class="mca" style="left:220px;top:193px;font-size:19px;color:var(--blue)">MCA</div>
  <div class="benefit" style="left:258px;top:205px;font-size:5.8px;color:var(--blue)"><svg width="12" height="10"><use href="#tick"/></svg>No personal guarantee</div>
  <div class="benefit" style="left:258px;top:219px;font-size:5.8px;color:var(--blue)"><svg width="12" height="10"><use href="#tick"/></svg>No minimum credit score</div>
  <div class="benefit" style="left:258px;top:233px;font-size:5.8px;color:var(--blue)"><svg width="12" height="10"><use href="#tick"/></svg>No collateral or guarantors needed</div>
  <div class="benefit" style="left:258px;top:247px;font-size:5.8px;color:var(--blue)"><svg width="12" height="10"><use href="#tick"/></svg>Bankruptcy – OK</div>
  <div style="left:393px;top:178px;width:30px;text-align:center;color:var(--lime);font-weight:500;font-size:9px;line-height:1.15">BANK<br>LOAN</div>
  <svg class="cross" style="left:401px;top:206px" width="12" height="12"><use href="#cross"/></svg>
  <svg class="cross" style="left:401px;top:220px" width="12" height="12"><use href="#cross"/></svg>
  <svg class="cross" style="left:401px;top:234px" width="12" height="12"><use href="#cross"/></svg>
  <svg class="cross" style="left:401px;top:248px" width="12" height="12"><use href="#cross"/></svg>
  <div class="apply" style="left:219px;top:267px;font-size:11.5px;color:var(--lime)">Simple one page application</div>
</section>
<div class="size-label" style="left:230px;top:1047px">8X5.5</div>

<!-- 5 x 7 -->
<section class="flyer" style="left:524px;top:726px;width:270px;height:377px">
  <div class="photo" role="img" aria-label="Close-up photograph of a fan of hundred dollar banknotes" style="height:180px"></div>
  <div class="headline" style="left:17px;top:8px;font-size:29px;line-height:34.5px">
    <span class="block">Say “Hello”</span><span class="block">To A</span><span class="block">Better Way</span><span class="block">To <span class="borrow">BORROW</span></span>
  </div>
  <div class="tagline" style="left:123px;top:146px;width:147px;height:23px;padding:1px 4px;font-size:7.3px;line-height:1.45">A convenient alternative to Bank Loan<br>Get Business Capital Cash Advance</div>

  <div style="left:0;top:180px;width:232px;height:19px;background:var(--white)"></div>
  <div style="left:0;top:199px;width:232px;height:111px;background:var(--sky)"></div>
  <div style="left:0;top:232px;width:35px;height:70px;background:var(--green-soft)"></div>
  <div style="left:0;top:302px;width:35px;height:36px;background:var(--lime-block)"></div>
  <div style="left:232px;top:218px;width:38px;height:61px;background:var(--green-pale)"></div>
  <div style="left:232px;top:310px;width:38px;height:28px;background:var(--white)"></div>
  <div class="bank-head" style="left:232px;top:180px;width:38px;height:38px;font-size:10px"><span>BANK</span><span>LOAN</span></div>

  <div class="mca" style="left:53px;top:204px;font-size:21px">MCA</div>
  <div class="benefit" style="left:93px;top:218px;font-size:5.6px"><svg width="12" height="11"><use href="#tick"/></svg>No personal guarantee</div>
  <div class="benefit" style="left:93px;top:233px;font-size:5.6px"><svg width="12" height="11"><use href="#tick"/></svg>No minimum credit score</div>
  <div class="benefit" style="left:93px;top:248px;font-size:5.6px"><svg width="12" height="11"><use href="#tick"/></svg>No collateral or guarantors needed</div>
  <div class="benefit" style="left:93px;top:263px;font-size:5.6px"><svg width="12" height="11"><use href="#tick"/></svg>Bankruptcy – OK</div>
  <svg class="cross" style="left:244px;top:219px" width="13" height="13"><use href="#cross"/></svg>
  <svg class="cross" style="left:244px;top:234px" width="13" height="13"><use href="#cross"/></svg>
  <svg class="cross" style="left:244px;top:249px" width="13" height="13"><use href="#cross"/></svg>
  <svg class="cross" style="left:244px;top:264px" width="13" height="13"><use href="#cross"/></svg>

  <div class="apply" style="left:47px;top:292px;font-size:10.5px">Simple one page application</div>
  <div class="inquire" style="left:39px;top:321px;font-size:5px;line-height:1.1">Inquire at<br><b style="font-size:7.5px">funding@example.com</b></div>

  <div class="bar" style="top:338px;height:39px">
    <span class="bar-title" style="left:8px;top:6px;font-size:17px">MERCHANT CASH ADVANCE</span>
    <span class="call" style="left:172px;top:5px"><em style="font-size:8.5px">Call Now</em><span class="phone" style="font-size:13px;line-height:1.1;padding-left:14px">555 013 2740</span></span>
  </div>
</section>
<div class="size-label" style="left:663px;top:1124px">5X7</div>

</body>
</html>
```